My project benefits Military, First Responders, Police, Fire, and Educators.

Contact Information for Business Card

2 Sided appointment card. Visual side will have my head shot with "Summit Venture" in a bold graffic/text. I am picturing maybe the headshot applied to a filter that has a matrix effect where the picture is made up of data/numbers flowing vertically through the photo. I am of course open to other concepts as well. Side two will have contact info presented in an attractive visual complimenting the front.

```html
<!DOCTYPE html>
<html lang="en">
<head>
<meta charset="utf-8">
<title>Summit Venture – Appointment Card</title>
<link rel="stylesheet" href="https://fonts.googleapis.com/css2?family=Open+Sans:wght@400;600&family=Oswald:wght@500&display=swap">
<style>
  :root {
    --page: #ffffff;
    --card-black: #1c1c1e;
    --card-light: #f2f2f2;
    --blue-bright: #29a8e0;
    --blue-deep: #1a78c9;
    --blue-pale: #5cc4ee;
    --text-white: #ffffff;
    --text-dark: #1e1e1e;
    --photo-warm: #6b3e22;
    --photo-dark: #3a2416;
    --photo-suit: #1f2a44;
  }
  html, body {
    margin: 0;
    width: 1200px;
    height: 1026px;
    overflow: hidden;
    background: var(--page);
  }
  .sheet {
    position: relative;
    width: 1200px;
    height: 1026px;
  }
  .card {
    position: absolute;
    top: 350px;
    width: 540px;
    height: 325px;
    display: block;
    box-shadow: 0 2px 6px rgba(0,0,0,0.12);
  }
  .card--front { left: 40px; }
  .card--back { left: 620px; }
  .logo-text {
    font-family: "Open Sans", sans-serif;
    font-weight: 600;
    font-size: 20px;
  }
  .audience-text {
    font-family: "Open Sans", sans-serif;
    font-weight: 400;
    font-size: 11.5px;
    fill: var(--blue-bright);
  }
  .person-name {
    font-family: "Oswald", sans-serif;
    font-weight: 500;
    font-size: 21px;
    fill: var(--blue-bright);
  }
  .person-role {
    font-family: "Open Sans", sans-serif;
    font-size: 8px;
    fill: var(--blue-bright);
  }
  .contact-text {
    font-family: "Open Sans", sans-serif;
    font-size: 13px;
    fill: var(--text-white);
  }
</style>
</head>
<body>
<main class="sheet">

  <!-- Front side -->
  <svg class="card card--front" viewBox="0 0 460 277" preserveAspectRatio="none">
    <defs>
      <linearGradient id="headshotTone" x1="0" y1="0" x2="0" y2="1">
        <stop offset="0" stop-color="var(--photo-warm)"/>
        <stop offset="0.6" stop-color="var(--photo-dark)"/>
        <stop offset="1" stop-color="var(--photo-suit)"/>
      </linearGradient>
    </defs>
    <rect class="card-base" width="460" height="277" fill="var(--card-black)"/>
    <g role="img" aria-label="Headshot of the card owner in suit and tie against a wooden door">
      <polygon class="headshot-area" points="118,0 460,0 460,277 236,277 262,232" fill="url(#headshotTone)"/>
    </g>
    <polygon class="chevron-outer" points="98,0 118,0 262,232 236,277 206,277 248,226" fill="var(--blue-bright)"/>
    <polygon class="chevron-inner" points="106,0 112,0 252,228 214,277 208,277 246,228" fill="var(--blue-pale)"/>
    <text class="logo-text" x="107" y="151" text-anchor="middle" fill="var(--text-white)">LOGO HERE</text>
    <text class="audience-text" x="125" y="207" text-anchor="middle">MILITARY</text>
    <text class="audience-text" x="125" y="223" text-anchor="middle">FIRST RESPONDERS</text>
    <text class="audience-text" x="125" y="239" text-anchor="middle">POLICE, FIRE, AND EDUCATORS</text>
  </svg>

  <!-- Back side -->
  <svg class="card card--back" viewBox="0 0 460 277" preserveAspectRatio="none">
    <rect class="card-base" width="460" height="277" fill="var(--card-light)"/>
    <polygon class="stripe-deep" points="300,0 460,0 460,277 125,277" fill="var(--blue-deep)"/>
    <polygon class="stripe-bright" points="310,0 460,0 460,277 140,277" fill="var(--blue-bright)"/>
    <polygon class="contact-panel" points="322,0 460,0 460,277 160,277" fill="var(--card-black)"/>
    <text class="logo-text" x="117" y="143" text-anchor="middle" fill="var(--text-dark)">LOGO HERE</text>
    <text class="person-name" x="358" y="78" text-anchor="middle">MR. ALDEN PRYCE</text>
    <text class="person-role" x="358" y="92" text-anchor="middle">MANAGING DIRECTOR</text>

    <g class="icon-phone" fill="var(--blue-bright)" transform="translate(261,145)">
      <path d="M2 1 L5 0 L7 4 L5 5.5 Q6.5 8.5 9 10 L10.5 8 L14 10 L13 13 Q5 13 2 1 Z"/>
    </g>
    <text class="contact-text" x="285" y="157">555-014-2291</text>

    <g class="icon-home" fill="var(--blue-bright)" transform="translate(260,174)">
      <polygon points="7.5,0 15,7 13,7 13,13 9.5,13 9.5,9 5.5,9 5.5,13 2,13 2,7 0,7"/>
    </g>
    <text class="contact-text" x="285" y="186">48 cedar lane elko</text>

    <g class="icon-web" fill="none" stroke="var(--blue-bright)" stroke-width="1.4" transform="translate(261,203)">
      <circle cx="7" cy="7" r="6.3" fill="var(--blue-bright)"/>
      <path d="M0.7 7 H13.3 M7 0.7 V13.3 M2 3.5 H12 M2 10.5 H12" stroke="var(--card-black)" stroke-width="1"/>
    </g>
    <text class="contact-text" x="285" y="215">alden48@mailbox.net</text>
  </svg>

</main>
</body>
</html>
```